Corvale Enterprises -Business Card Design Project

I have a new logo to put onto business cards - attached
The word doc shows how I want it all laid out - front page and rear
The lettering I want is clean and rounded - modern
Reason: There was no original deadline!
Target Market(s)
25-49 year old leaders and entrepreneurs in Australia
Industry/Entity Type
Business

```html
<!DOCTYPE html>
<html lang="en">
<head>
<meta charset="utf-8">
<title>Corvale Enterprises – Business Card</title>
<link rel="stylesheet" href="https://fonts.googleapis.com/css2?family=Nunito:wght@400;600;800&display=swap">
<style>
  :root {
    --backdrop: #e8e8e8;
    --card: #ffffff;
    --brand-blue: #1f5aa8;
    --brand-blue-dark: #174a8f;
    --swoosh-grey: #b9bcc0;
    --text-grey: #555a60;
    --white: #ffffff;
  }
  html, body {
    margin: 0;
    width: 1200px;
    height: 718px;
    overflow: hidden;
    background: var(--backdrop);
    font-family: "Nunito", sans-serif;
  }
  .business-card {
    position: absolute;
    left: 130px;
    top: 96px;
    width: 940px;
    height: 526px;
    background: var(--card);
    box-shadow: 0 12px 30px rgba(0,0,0,0.12);
    overflow: hidden;
  }
  .swoosh {
    position: absolute;
    inset: 0;
    width: 100%;
    height: 100%;
  }
  .brand {
    position: absolute;
    left: 78px;
    top: 196px;
    display: flex;
    align-items: center;
    gap: 18px;
  }
  .brand-mark {
    width: 62px;
    height: 62px;
    background: var(--brand-blue);
  }
  .brand-name {
    font-weight: 800;
    font-size: 34px;
    line-height: 1.05;
    letter-spacing: 4px;
    color: var(--brand-blue);
    text-transform: uppercase;
  }
  .person {
    position: absolute;
    right: 70px;
    top: 60px;
    text-align: right;
  }
  .person-name {
    margin: 0;
    font-weight: 800;
    font-size: 30px;
    letter-spacing: 1.5px;
    color: var(--brand-blue);
    text-transform: uppercase;
  }
  .person-role {
    margin: 4px 0 0;
    font-weight: 600;
    font-size: 15px;
    letter-spacing: 2px;
    color: var(--text-grey);
    text-transform: uppercase;
  }
  .contact-list {
    position: absolute;
    right: 70px;
    top: 164px;
    margin: 0;
    padding: 0;
    list-style: none;
  }
  .contact-item {
    display: flex;
    justify-content: flex-end;
    align-items: center;
    gap: 12px;
    height: 32px;
    font-size: 16px;
    font-weight: 600;
    color: var(--text-grey);
  }
  .contact-icon {
    width: 18px;
    height: 18px;
    fill: var(--brand-blue);
  }
  .address {
    position: absolute;
    left: 60px;
    bottom: 34px;
    margin: 0;
    font-style: normal;
    font-weight: 600;
    font-size: 19px;
    line-height: 1.4;
    color: var(--white);
    letter-spacing: 0.5px;
  }
</style>
</head>
<body>
  <main class="business-card">
    <svg class="swoosh" viewBox="0 0 940 526" preserveAspectRatio="none" aria-hidden="true">
      <path fill="var(--swoosh-grey)" d="M0 430 C 260 400, 560 390, 940 250 L 940 290 C 600 420, 300 430, 0 455 Z"/>
      <path fill="var(--brand-blue)" d="M0 440 C 300 420, 600 410, 940 280 L 940 526 L 0 526 Z"/>
      <path fill="var(--brand-blue-dark)" d="M500 526 C 700 470, 840 400, 940 340 L 940 526 Z" opacity="0.35"/>
    </svg>

    <div class="brand">
      <div class="brand-mark"></div>
      <div class="brand-name">Corvale<br>Enterprises</div>
    </div>

    <header class="person">
      <h1 class="person-name">Daniel Harwick</h1>
      <p class="person-role">Financial Advisor</p>
    </header>

    <ul class="contact-list">
      <li class="contact-item">021 468 3570
        <svg class="contact-icon" viewBox="0 0 24 24"><path d="M6.6 10.8a15.1 15.1 0 0 0 6.6 6.6l2.2-2.2a1 1 0 0 1 1-.25 11.4 11.4 0 0 0 3.6.57 1 1 0 0 1 1 1V20a1 1 0 0 1-1 1A17 17 0 0 1 3 4a1 1 0 0 1 1-1h3.5a1 1 0 0 1 1 1c0 1.25.2 2.45.57 3.57a1 1 0 0 1-.25 1z"/></svg>
      </li>
      <li class="contact-item">021 468 3571
        <svg class="contact-icon" viewBox="0 0 24 24"><rect x="6" y="2" width="12" height="20" rx="2"/><rect x="8" y="5" width="8" height="12" fill="#fff"/></svg>
      </li>
      <li class="contact-item">hello@corvale.example
        <svg class="contact-icon" viewBox="0 0 24 24"><rect x="2" y="5" width="20" height="14" rx="1.5"/><path d="M3 6l9 7 9-7" stroke="#fff" stroke-width="1.8" fill="none"/></svg>
      </li>
      <li class="contact-item">www.corvale.example
        <svg class="contact-icon" viewBox="0 0 24 24"><circle cx="12" cy="12" r="10"/><path d="M2 12h20M12 2c3 3 3 17 0 20M12 2c-3 3-3 17 0 20" stroke="#fff" stroke-width="1.4" fill="none"/></svg>
      </li>
    </ul>

    <address class="address">14/2, 9th Floor Arcade<br>Wattle Street NSW</address>
  </main>
</body>
</html>
```